Take Out Menu

We are looking to redo our take out menu.
See current attached file for our current design.
The menu should make you hungry when looking at the pictures.
Target Market(s)
All of our customers.
Industry/Entity Type
Restaurant
Contact Information for Business Card
I will attach an image of our current card. It has the details of what we need on it.
Colors
Designer to choose colors to be used in the design.
Requirements
Must have
- A fresh look and feel. We must use our current logo branding. You can look at Velkoran on google to see what our restaurants look like.
Nice to have
- Easy read with food pictures.

```html
<!DOCTYPE html>
<html lang="en">
<head>
<meta charset="utf-8">
<title>Velkoran Business Card</title>
<link rel="stylesheet" href="https://fonts.googleapis.com/css2?family=Arimo:wght@400;700&display=swap">
<style>
  :root {
    --backdrop: #aaa6a6;
    --brand-red: #b21f24;
    --accent-yellow: #f5d31a;
    --text-light: #ffffff;
    --text-dark: #1d1d1d;
    --wood-light: #f3e1c6;
    --wood-mid: #e6c9a2;
    --map-base: #e8e8e8;
    --map-road: #f7f7f7;
    --road-yellow-tint: rgba(245, 211, 26, 0.42);
    --road-red-tint: rgba(178, 31, 36, 0.22);
  }
  * { box-sizing: border-box; margin: 0; padding: 0; }
  html, body {
    width: 1200px; height: 1200px; overflow: hidden;
    background: var(--backdrop);
    font-family: "Arimo", Arial, sans-serif;
  }
  .canvas { position: relative; width: 1200px; height: 1200px; }
  .card {
    position: absolute; top: 133px;
    width: 482px; height: 843px; overflow: hidden;
  }
  .card-front { left: 97px; background: var(--brand-red); }
  .card-back { left: 633px; }

  .brand-header {
    position: absolute; left: 0; top: 0; width: 100%; height: 395px;
    background: linear-gradient(180deg, var(--wood-light), var(--wood-mid));
  }
  .brand-name {
    position: absolute; left: 0; top: 222px; width: 100%;
    text-align: center; font-weight: 700; font-size: 80px;
    color: var(--brand-red); letter-spacing: 1px;
  }

  .contact { position: absolute; left: 0; width: 100%; text-align: center; color: var(--text-light); font-weight: 700; line-height: 1.2; }
  .address-line { font-size: 31px; }
  .street { top: 598px; transform: translateY(-100%); top: 636px; }
  .unit {
    top: 642px; display: flex; align-items: center; justify-content: center; gap: 16px;
  }
  .unit .rule { display: block; width: 104px; height: 2px; background: var(--text-light); }
  .city { top: 689px; }
  .city .town { color: var(--accent-yellow); }
  .street { top: 596px; transform: none; }
  .unit { top: 642px; }
  .city { top: 689px; }
  .street, .unit, .city { margin-top: -133px; }
  .contact-icon { position: absolute; left: 50%; transform: translateX(-50%); }
  .phone-icon { top: 617px; }
  .web-icon { top: 715px; }
  .phone { top: 650px; font-size: 39px; }
  .web { top: 746px; font-size: 37px; }

  .location-map {
    position: absolute; inset: 0;
    background:
      linear-gradient(132deg, transparent 30%, var(--road-red-tint) 52%, transparent 74%),
      linear-gradient(40deg, transparent 28%, var(--road-yellow-tint) 50%, transparent 72%),
      linear-gradient(160deg, var(--map-road), var(--map-base) 60%, #e2e2e2);
  }
  .map-pin { position: absolute; left: 206px; top: 305px; }
  .map-label {
    position: absolute; left: 0; top: 356px; width: 100%;
    text-align: center; font-weight: 700; font-size: 19px; line-height: 25px;
    color: var(--text-dark);
  }
</style>
</head>
<body>
<main class="canvas">
  <section class="card card-front">
    <div class="brand-header" role="img" aria-label="Light wooden plank background with palm trees on a small island"></div>
    <div class="brand-name">Velkoran</div>

    <div class="contact address-line street">2480 Harrowfield Rd</div>
    <div class="contact address-line unit"><span class="rule"></span>Unit 7B<span class="rule"></span></div>
    <div class="contact address-line city"><span class="town">Millbrook</span>, ON K9A 3T2</div>

    <svg class="contact-icon phone-icon" width="28" height="24" viewBox="0 0 26 22" aria-hidden="true">
      <path d="M2 7 C2 2 24 2 24 7 L20 8 L19 5 C15 4 11 4 7 5 L6 8 Z" fill="var(--accent-yellow)"/>
      <path d="M8 8 L18 8 L22 20 L4 20 Z" fill="var(--accent-yellow)"/>
      <circle cx="13" cy="14" r="3" fill="var(--brand-red)"/>
    </svg>
    <div class="contact phone">905 555 0142</div>

    <svg class="contact-icon web-icon" width="26" height="26" viewBox="0 0 24 24" aria-hidden="true">
      <g fill="none" stroke="var(--accent-yellow)" stroke-width="2">
        <circle cx="12" cy="12" r="10"/>
        <ellipse cx="12" cy="12" rx="4.5" ry="10"/>
        <line x1="2" y1="12" x2="22" y2="12"/>
        <line x1="4" y1="6.5" x2="20" y2="6.5"/>
        <line x1="4" y1="17.5" x2="20" y2="17.5"/>
      </g>
    </svg>
    <div class="contact web">www.velkoran.com</div>
  </section>

  <section class="card card-back">
    <div class="location-map" role="img" aria-label="Street map showing the restaurant beside the crossing of two main roads, one shown in yellow and one in red"></div>
    <svg class="map-pin" width="28" height="36" viewBox="0 0 26 34" aria-hidden="true">
      <path d="M13 0 C5.8 0 0 5.8 0 13 C0 22 13 34 13 34 C13 34 26 22 26 13 C26 5.8 20.2 0 13 0 Z" fill="var(--brand-red)"/>
      <circle cx="13" cy="12.5" r="5" fill="var(--map-base)"/>
    </svg>
    <div class="map-label">VELKORAN<br>RESTAURANT</div>
  </section>
</main>
</body>
</html>
```